Tobias Wrenfield - Cinematographer

NEED:
I'm looking for a sleek, professional, modern business card that will give give the recipient the impression that they can trust their production will go smoothly by hiring me. I will bring creativity and knowledge to their shoot, so that we can create powerful images.
I am looking for a card with a strong style and design ethos that could be expanded to a website and a full visual/graphic/design entity for me.
ABOUT ME:
I am a mid-twenties cinematographer, I work on music video, narrative short, commercial, and corporate projects. I blend the science and artistry of cameras and filmmaking to tell a story. I'm an artist, a technician, and a manager.
DESIGN:
I like sleek, simple design. Black, dark grays, white, dark navy, steel blues, I love cyan, but also cyan and red. I am not a fan of earthy tones. I generally prefer modern, san-serif fonts over serifs. My old logo was based on an aperture, a multi-blade device at the back of a lens that controls how much light passes through, but I made it with so many colors, that it doesn't necessarily lend itself to a specific color-scheme or design ethos. I liked that the aperture design provided a sense of the technical requirements of my job. I'm a fan of matte business cards, but am open to plenty of specialty print processes to make an outstanding card.
ATTACHED FILES:
My Old Rainbox Aperture Logo, plus a few designs I've tried playing around with, but am not tied to. I AM OPEN TO NEW DESIGNS, DO NOT FEEL TIED TO THIS.
**I've pulled my old logo down from the attached files, and instead attached other business cards I like, so as not to mislead you where I would like to go.
INFO:
Name: Tobias Wrenfield
Job: Cinematographer
Email: tkwrenfield@quillbox.example
Phone: 503.618.2907
Website: tobiaswrenfield.example
Updates
I'm adding some images of other cards that I like, and removing my old logo, since I'm looking for something new, and don't want that old logo to push anyone a certain direction.

```html
<!DOCTYPE html>
<html lang="en">
<head>
<meta charset="utf-8">
<title>Tobias Wrenfield – Cinematographer Business Card</title>
<link rel="stylesheet" href="https://fonts.googleapis.com/css2?family=Teko:wght@400;500&family=Roboto+Condensed:wght@400;700&display=swap">
<style>
  :root {
    --teal: #0b95a5;
    --ink: #111111;
    --paper: #f3f3f3;
    --white: #ffffff;
    --grey-text: #555555;
    --backdrop: #d9dcde;
    --card-w: 665px;
    --card-h: 380px;
  }
  * { box-sizing: border-box; margin: 0; padding: 0; }
  html, body {
    width: 1200px;
    height: 900px;
    overflow: hidden;
    background: var(--backdrop);
  }
  .canvas {
    width: 1200px;
    height: 900px;
    display: flex;
    flex-direction: column;
    align-items: center;
    justify-content: center;
    gap: 40px;
  }
  .card {
    position: relative;
    width: var(--card-w);
    height: var(--card-h);
    overflow: hidden;
    box-shadow: 0 6px 18px rgba(0, 0, 0, 0.18);
  }

  /* Front */
  .card--front {
    background: var(--teal);
    display: flex;
    align-items: center;
    justify-content: center;
  }
  .front-badge {
    width: 210px;
    height: 210px;
    border-radius: 50%;
    background: var(--ink);
    display: flex;
    flex-direction: column;
    align-items: center;
    justify-content: center;
    color: var(--white);
    font-family: "Teko", sans-serif;
    font-weight: 400;
    font-size: 40px;
    line-height: 0.9;
    letter-spacing: 4px;
    text-transform: uppercase;
  }

  /* Back */
  .card--back {
    background: var(--paper);
  }
  .contact {
    position: absolute;
    left: 62px;
    top: 142px;
    display: grid;
    grid-template-columns: 90px auto;
    row-gap: 9px;
    font-family: "Roboto Condensed", sans-serif;
    font-size: 10px;
    letter-spacing: 1.6px;
    text-transform: uppercase;
  }
  .contact__label {
    font-weight: 700;
    color: var(--ink);
  }
  .contact__value {
    font-weight: 400;
    color: var(--grey-text);
    padding-left: 10px;
  }
  .identity-disc {
    position: absolute;
    width: 290px;
    height: 290px;
    border-radius: 50%;
    background: var(--teal);
    left: 420px;
    top: 108px;
    display: flex;
    flex-direction: column;
    justify-content: center;
    padding-left: 34px;
    color: var(--white);
    text-transform: uppercase;
    font-family: "Teko", sans-serif;
  }
  .identity-disc__name {
    font-weight: 500;
    font-size: 44px;
    line-height: 0.88;
    letter-spacing: 5px;
  }
  .identity-disc__role {
    margin-top: 6px;
    font-weight: 400;
    font-size: 21px;
    letter-spacing: 3.5px;
  }
</style>
</head>
<body>
  <main class="canvas">
    <section class="card card--front" aria-label="Business card front">
      <div class="front-badge">
        <span>Tobias</span>
        <span>Wrenfield</span>
      </div>
    </section>

    <section class="card card--back" aria-label="Business card back">
      <div class="contact">
        <span class="contact__label">Email</span>
        <span class="contact__value">tkwrenfield@quillbox.example</span>
        <span class="contact__label">Phone</span>
        <span class="contact__value">503.618.2907</span>
        <span class="contact__label">Website</span>
        <span class="contact__value">tobiaswrenfield.example</span>
      </div>
      <div class="identity-disc">
        <span class="identity-disc__name">Tobias<br>Wrenfield</span>
        <span class="identity-disc__role">Cinematographer</span>
      </div>
    </section>
  </main>
</body>
</html>
```